Client Meeting and installation Email Follow up

I would like a follow-up email template created.
Currently, we do a lot of new construction builds and meet with clients about 6-3 months before they take possession of their new house. I want a follow-up email template to be sent after the homeowner takes possession of their house that enquires if the clients are happy about their new lighting, the service they received, and their customer service representative with Meridale Glow and Breeze. I have attached a few files of what our current marketing looks like.
Target Market(s)
Home Owners We have already met with
Industry/Entity Type
Residential lighting
Font styles to use
Other font styles liked:
- Alta Light, Playfair Display, Montserrat
Colors
Designer to choose colors to be used in the design.
Look and feel
Each slider illustrates characteristics of the customer's brand and the style your logo design should communicate.

```html
<!DOCTYPE html>
<html lang="en">
<head>
<meta charset="UTF-8">
<title>Meridale Glow and Breeze – Thank You</title>
<link href="https://fonts.googleapis.com/css2?family=Bellefair&family=Poppins:wght@400;500;600;700&display=swap" rel="stylesheet">
<style>
  :root {
    --paper: #ffffff;
    --ink: #111111;
    --ink-soft: #4a4744;
    --linen: #e9e4dc;
    --linen-deep: #d8cdbd;
    --room-light: #ece9e4;
    --room-wood: #c9b79c;
    --room-sage: #b9bfae;
    --room-stone: #8f8b80;
  }
  * { margin: 0; padding: 0; box-sizing: border-box; }
  html, body { width: 848px; height: 1200px; overflow: hidden; background: var(--paper); }
  .email {
    position: relative;
    width: 848px;
    height: 1200px;
    background: var(--paper);
    color: var(--ink);
    font-variant-numeric: lining-nums;
  }
  .hero-photo {
    position: absolute;
    left: 0; top: 0;
    width: 848px; height: 199px;
    background: linear-gradient(100deg, var(--linen) 0%, #f3f0eb 45%, var(--linen-deep) 80%, #f1eee9 100%);
  }
  .brand-plate {
    position: absolute;
    left: 221px; top: 27px;
    width: 396px; height: 131px;
    background: var(--paper);
    display: flex;
    align-items: center;
    justify-content: center;
    text-align: center;
    padding: 0 18px;
  }
  .brand-name {
    font-family: "Bellefair", serif;
    font-size: 40px;
    line-height: 1.1;
    color: var(--ink);
    letter-spacing: 1px;
  }
  .check-in {
    position: absolute;
    left: 110px; top: 228px;
    width: 628px;
    text-align: center;
    font-family: "Poppins", sans-serif;
    font-weight: 400;
    font-size: 16px;
    line-height: 1.6;
    color: var(--ink-soft);
  }
  .headline {
    position: absolute;
    left: 0; top: 330px;
    width: 848px;
    text-align: center;
    font-family: "Bellefair", serif;
    font-weight: 400;
    font-size: 142px;
    line-height: 1;
  }
  .divider {
    position: absolute;
    left: 98px; top: 527px;
    width: 652px; height: 3px;
    background: var(--ink);
  }
  .offer {
    position: absolute;
    left: 0; top: 540px;
    width: 848px;
    text-align: center;
    font-family: "Bellefair", serif;
    font-size: 136px;
    line-height: 1;
  }
  .promo-code {
    position: absolute;
    left: 0; top: 713px;
    width: 848px;
    text-align: center;
    font-family: "Poppins", sans-serif;
    font-weight: 700;
    font-size: 30px;
    letter-spacing: 1px;
  }
  .room-photo {
    position: absolute;
    top: 824px;
    height: 376px;
  }
  .room-photo--left {
    left: 0; width: 420px;
    background: linear-gradient(180deg, var(--room-light) 0%, #f5f4f1 55%, var(--room-wood) 100%);
  }
  .room-photo--right {
    left: 428px; width: 420px;
    background: linear-gradient(180deg, #e8e6df 0%, var(--room-sage) 50%, var(--room-stone) 100%);
  }
  .shop-button {
    position: absolute;
    left: 281px; top: 982px;
    width: 287px; height: 59px;
    border-radius: 30px;
    background: var(--paper);
    display: flex;
    align-items: center;
    justify-content: center;
    font-family: "Poppins", sans-serif;
    font-weight: 600;
    font-size: 19px;
    color: var(--ink);
    text-decoration: none;
  }
</style>
</head>
<body>
  <main class="email">
    <div class="hero-photo" role="img" aria-label="Bright living space with macramé hammock, woven basket and driftwood decor"></div>
    <div class="brand-plate">
      <span class="brand-name">Meridale Glow and Breeze</span>
    </div>

    <p class="check-in">Welcome home! Are you happy with your new lighting, the service you received and your customer service representative? Simply reply and let us know.</p>

    <h1 class="headline">Thank You</h1>
    <div class="divider"></div>
    <p class="offer">10% OFF</p>
    <p class="promo-code">USE CODE: ILOVELIGHTS</p>

    <div class="room-photo room-photo--left" role="img" aria-label="White dining room with black candle-style chandelier over a long table and wishbone chairs"></div>
    <div class="room-photo room-photo--right" role="img" aria-label="Dining room with botanical wallpaper, round mirror and a black and brass chandelier"></div>

    <a class="shop-button" href="#">SHOP NOW!</a>
  </main>
</body>
</html>
```